Business Cards Design for the electrical wholesaler: clean bold dynamic :)

We need a business card design that would follow our latest brand guidelines. As an electrical wholesaler we want to bring a fresh look and feel into the industry. The design should be clean bold and dynamic. It should come alive with the renewed energy of our green colour. Our grey colour should keep things balanced and complement the notion of maturity and responsibility. We employ Lato as a corporate font however are not bound by this font and we’re open to interpretation here.

Target Market(s)

Electrical contractors

Industry/Entity Type

Business

Contact Information for Business Card

Logo
Name & Surname: Olena Dovbush
Job Title: Director of Marketing
Email: helen.dovbush@mailvane.example
Cell phone: XXX.XXX.XXXX
Address: 20917 - 87 Ave. Edmonton, AB, Canada. T6K 2R8
Business Phone: 780.555.0187
Website: www.qorvil.example

Font styles to use
Other font styles liked:
• Lato

Requirements
Must have
• Logo & website
Nice to have
• Brand elements - some of them you may find in the attached Brand Guidelines (e.g. three lines on the background signifying "W")

```html
<!DOCTYPE html>
<html lang="en">
<head>
<meta charset="utf-8">
<title>Qorvil – Business Cards</title>
<link href="https://fonts.googleapis.com/css2?family=Open+Sans:wght@400;700&display=swap" rel="stylesheet">
<style>
  :root {
    --brand-green: #8cc63f;
    --brand-grey: #4a4b4d;
    --text-grey: #3d3e40;
    --card-white: #ffffff;
    --backdrop: #e4e5e7;
  }
  * { box-sizing: border-box; margin: 0; padding: 0; }
  html, body {
    width: 1200px;
    height: 900px;
    overflow: hidden;
    background: var(--backdrop);
    font-family: "Open Sans", sans-serif;
    color: var(--text-grey);
  }
  .canvas {
    position: relative;
    width: 1200px;
    height: 900px;
  }
  .card {
    position: absolute;
    left: 320px;
    width: 560px;
    height: 320px;
    background: var(--card-white);
    border-radius: 28px;
    box-shadow: 0 6px 18px rgba(0,0,0,0.12);
    overflow: hidden;
  }
  .card--contact { top: 100px; }
  .card--brand { top: 480px; }

  .wordmark {
    display: flex;
    align-items: center;
    gap: 10px;
    color: var(--brand-grey);
    font-weight: 400;
    line-height: 1;
  }
  .wordmark__dot {
    border-radius: 50%;
    background: var(--brand-green);
    flex: none;
  }
  .card--contact .wordmark {
    position: absolute;
    left: 40px;
    top: 40px;
    font-size: 44px;
  }
  .card--contact .wordmark__dot { width: 34px; height: 34px; }

  .company-details {
    position: absolute;
    right: 40px;
    top: 112px;
    text-align: right;
    font-size: 15px;
    line-height: 1.4;
  }
  .person-details {
    position: absolute;
    left: 40px;
    bottom: 36px;
    font-size: 16px;
    line-height: 1.35;
  }
  .person-details__name,
  .person-details__title { font-weight: 700; }

  .card--brand .wordmark {
    position: absolute;
    left: 0;
    right: 0;
    top: 0;
    bottom: 0;
    justify-content: center;
    gap: 22px;
    font-size: 104px;
  }
  .card--brand .wordmark__dot { width: 78px; height: 78px; }
</style>
</head>
<body>
<main class="canvas">
  <section class="card card--contact" aria-label="Business card, contact side">
    <div class="wordmark">
      <span class="wordmark__dot"></span>
      <span class="wordmark__name">qorvil</span>
    </div>
    <address class="company-details" style="font-style: normal;">
      <p>20917 - 87 Ave.</p>
      <p>Edmonton, AB, Canada. T6K 2R8</p>
      <p>780.555.0187</p>
      <p>www.qorvil.example</p>
    </address>
    <div class="person-details">
      <p class="person-details__name">Olena Dovbush</p>
      <p class="person-details__title">Director of Marketing</p>
      <p class="person-details__email">helen.dovbush@mailvane.example</p>
      <p class="person-details__phone">Cell phone: XXX.XXX.XXXX</p>
    </div>
  </section>

  <section class="card card--brand" aria-label="Business card, brand side">
    <div class="wordmark">
      <span class="wordmark__dot"></span>
      <span class="wordmark__name">qorvil</span>
    </div>
  </section>
</main>
</body>
</html>
```